Banner ad design for Vantor Reach Ads

We are looking for a designer to develop a concept for banner ads for a Vantor Reach campaign we are building.

We have 3 business lines, shredding services, records management services and scanning services.

We are looking for 4 sets of ads to be created, one for each business line + one set that showcases all of our lines together.

For the design concepts, we would like to see a few sizes (banner, square, leaderboard, skyscraper, etc) for each.

The person chosen will then need to create the ads into all Vantor supported sizes -- 20 sizes total for each set of ads as per the Vantor size guidelines found on this page - https://help.vantor.example/vantor-ads/answer/4859210?hl=en&ref_topic=6082714#

A few items to note:
- Design should complement our existing brand/website look and feel (www.gold-kettle.ca)
- Each final ad must be 150Kb or less in size
- Final designs should be editable, meaning if we would like to change some copy in the design, we can do so using a well-known software (Canva, Photoshop/InDesign, etc)
- Some images are attached for use, but if you feel a different stock image is more suitable to to your design, please go ahead and use it.

Provided below is some messaging that can be used for each set of ads. Do not feel you need to use all of the messaging, it is provided for guidance.

SHREDDING SERVICES:

Possible Short Headline:
-- One-Time Shredding Services
-- Secure Shredding Services
-- Affordable On-Site Shredding

Possible Long Headline
-- Your Paper Can be Destroyed as Soon as the Next Business Day

Possible Descriptions:
-- QVRB AAA Certified On site shredding company. Service as soon as Next Day.
-- Secure and Affordable Toronto & GTA On-Site Shredding.
-- Certified, Affordable Office Shredding Since 2003.
-- Quick, no contact and affordable paper shredding services in Toronto & Southern Ontario.
-- Certified, Affordable Office Shredding Since 2003. Fast, no contact shredding service.

Call to Action
-- Get a Quote

RECORDS MANAGEMENT
Short Headline:
-- Off-site Records Storage
-- Records Management & Storage
-- Secure Records Storage
-- Records Management Services
-- Long Term Records Management
-- Document Storage Solutions

Possible Description
-- Local, Affordable Storage Solutions. Protect and Store your Documents in our Secure Facility
-- Local, Affordable Records Management Solutions. Store your Records in our Secure Facility
-- Certified, Affordable Document Storage Since 2004. Contact Us for a Free Quote!
-- Vaultmark+ Certified, Affordable Document Storage Since 2004. Contact Us for a Free Quote!

Call to Action
-- Get a Quote

SCANNING SERVICES

Short Headline:
-- Professional Scanning Company
-- Toronto & GTA Scanning Service
-- Document Scanning Services
-- Digital Conversion Services
-- Fast & Easy Retrieval

Description
-- Scan and documents and files with Professional scanning services from Gold-Kettle
-- Convert Your Paper Files to Electronic Files. Fast & Easy Retrieval.
-- Easily access your documents electronically with Document Scanning Services

Call to Action
-- Get a Quote

ALL SERVICES AD SET
Short Headline
-- Shred, Scan & Store Documents
-- Secure Shredding, Records Management and Scanning Services
-- #1 Document Management Company
-- Gold Kettle Shredding, Storage & Scanning

Description
-- Secure and Affordable Toronto & GTA On-Site Shredding, Document Storage & Scanning Company

Call to Action
-- Get a Quote

Font styles to use
Sans Serif

```html
<!DOCTYPE html>
<html lang="en">
<head>
<meta charset="utf-8">
<title>Vantor Reach Ads – Gold-Kettle Banner Set</title>
<link rel="stylesheet" href="https://fonts.googleapis.com/css2?family=Poppins:wght@400;500;600;700&display=swap">
<style>
  :root {
    --stage: #2a2a2a;
    --brand-blue: #0e86c9;
    --brand-blue-deep: #0a73b8;
    --brand-blue-light: #3aa6e0;
    --accent-green: #16b84a;
    --white: #ffffff;
  }
  * { margin: 0; padding: 0; box-sizing: border-box; }
  html, body { width: 769px; height: 1200px; overflow: hidden; }
  body {
    background: var(--stage);
    font-family: "Poppins", sans-serif;
    color: var(--white);
    position: relative;
  }
  .banner {
    position: absolute;
    left: 103px;
    width: 562px;
    height: 205px;
    overflow: hidden;
    background: var(--brand-blue);
    box-shadow: 0 6px 18px rgba(0,0,0,0.45);
  }
  .banner--scanning { top: 106px; }
  .banner--shredding { top: 366px; }
  .banner--records { top: 631px; }
  .banner--all { top: 896px; }

  .banner__art { position: absolute; inset: 0; width: 100%; height: 100%; }

  .banner__copy { position: absolute; }
  .banner__title {
    font-weight: 700;
    font-size: 19px;
    line-height: 21px;
    white-space: nowrap;
  }
  .banner__rule {
    width: 106px;
    height: 2px;
    background: var(--white);
    margin: 13px 0 12px;
  }
  .banner__text {
    font-weight: 400;
    font-size: 11.6px;
    line-height: 13.8px;
    white-space: nowrap;
  }
  .banner__cta {
    display: inline-block;
    width: 105px;
    height: 22px;
    line-height: 22px;
    text-align: center;
    background: var(--accent-green);
    color: var(--white);
    font-weight: 500;
    font-size: 13px;
    margin-top: 20px;
    box-shadow: 2px 3px 5px rgba(0,0,0,0.25);
  }

  .banner--scanning .banner__copy { left: 25px; top: 28px; }
  .banner--shredding .banner__copy { left: 334px; top: 32px; }
  .banner--shredding .banner__title { line-height: 23px; }
  .banner--records .banner__copy { left: 30px; top: 30px; }
  .banner--all .banner__copy { right: 30px; top: 31px; text-align: right; }
  .banner--all .banner__rule { margin-left: auto; }
</style>
</head>
<body>

  <section class="banner banner--scanning">
    <svg class="banner__art" viewBox="0 0 562 205" preserveAspectRatio="none">
      <defs>
        <linearGradient id="scanPhoto" x1="0" y1="0" x2="1" y2="1">
          <stop offset="0" stop-color="#d9dbe0"/>
          <stop offset="0.45" stop-color="#8e95a2"/>
          <stop offset="0.75" stop-color="#d0d3d8"/>
          <stop offset="1" stop-color="#efefee"/>
        </linearGradient>
      </defs>
      <rect width="562" height="205" fill="var(--brand-blue)"/>
      <path d="M275 0 L562 0 L562 205 L311 205 L334 66 Z" fill="url(#scanPhoto)" role="img" aria-label="Photo of a staff member loading paper documents into a scanner"/>
    </svg>
    <div class="banner__copy">
      <h2 class="banner__title">Document Scanning<br>Services</h2>
      <div class="banner__rule"></div>
      <p class="banner__text">Scan and documents and files with<br>Professional scanning services<br>from Gold-Kettle</p>
      <span class="banner__cta">Get a Quote</span>
    </div>
  </section>

  <section class="banner banner--shredding">
    <svg class="banner__art" viewBox="0 0 562 205" preserveAspectRatio="none">
      <defs>
        <linearGradient id="shredPhoto" x1="0" y1="0" x2="1" y2="1">
          <stop offset="0" stop-color="#efefec"/>
          <stop offset="0.55" stop-color="#d6d6d2"/>
          <stop offset="1" stop-color="#b4b8bd"/>
        </linearGradient>
      </defs>
      <rect width="562" height="205" fill="var(--brand-blue)"/>
      <path d="M0 0 L193 0 C290 20 318 110 316 205 L0 205 Z" fill="var(--brand-blue-light)"/>
      <path d="M0 0 L188 0 C278 22 304 110 302 205 L0 205 Z" fill="url(#shredPhoto)" role="img" aria-label="Photo of a hand placing papers into a secure shredding bin"/>
      <path d="M0 110 C10 170 40 200 80 205 L0 205 Z" fill="var(--brand-blue-light)" opacity="0.85"/>
    </svg>
    <div class="banner__copy">
      <h2 class="banner__title">One-Time Shredding<br>Services</h2>
      <div class="banner__rule"></div>
      <p class="banner__text">QVRB AAA Certified On site shredding<br>company. Service as soon<br>as Next Day.</p>
      <span class="banner__cta">Get a Quote</span>
    </div>
  </section>

  <section class="banner banner--records">
    <svg class="banner__art" viewBox="0 0 562 205" preserveAspectRatio="none">
      <defs>
        <linearGradient id="recordsPhoto" x1="0" y1="0" x2="1" y2="0">
          <stop offset="0" stop-color="#b7a78d"/>
          <stop offset="0.5" stop-color="#d8cdb8"/>
          <stop offset="1" stop-color="#a7a196"/>
        </linearGradient>
      </defs>
      <rect width="562" height="205" fill="var(--brand-blue)"/>
      <path d="M274 0 L300 0 L324 205 L266 205 L315 166 Z" fill="var(--accent-green)"/>
      <path d="M300 0 L562 0 L562 205 L324 205 Z" fill="url(#recordsPhoto)" role="img" aria-label="Photo of tall warehouse shelving filled with archive boxes"/>
    </svg>
    <div class="banner__copy">
      <h2 class="banner__title">Long Term Records<br>Management</h2>
      <div class="banner__rule"></div>
      <p class="banner__text">Local, Affordable Records Management<br>Solutions. Store your Records in our<br>Secure Facility</p>
      <span class="banner__cta">Get a Quote</span>
    </div>
  </section>

  <section class="banner banner--all">
    <svg class="banner__art" viewBox="0 0 562 205" preserveAspectRatio="none">
      <defs>
        <linearGradient id="allPerson" x1="0" y1="0" x2="1" y2="1">
          <stop offset="0" stop-color="#d6d8dc"/>
          <stop offset="0.6" stop-color="#7d8594"/>
          <stop offset="1" stop-color="#e2e3e5"/>
        </linearGradient>
        <linearGradient id="allShelves" x1="0" y1="0" x2="1" y2="0">
          <stop offset="0" stop-color="#b8a88e"/>
          <stop offset="1" stop-color="#d4c8b2"/>
        </linearGradient>
        <linearGradient id="allBin" x1="0" y1="0" x2="1" y2="1">
          <stop offset="0" stop-color="#ececea"/>
          <stop offset="1" stop-color="#c4c6c9"/>
        </linearGradient>
      </defs>
      <rect width="562" height="205" fill="var(--brand-blue)"/>
      <path d="M0 0 L96 0 L186 150 L90 205 L0 205 Z" fill="url(#allPerson)" role="img" aria-label="Photo of a staff member feeding documents into a scanner"/>
      <path d="M96 0 L385 0 L264 106 L186 150 Z" fill="url(#allShelves)" role="img" aria-label="Photo of warehouse shelving stacked with archive boxes"/>
      <path d="M186 150 L264 106 L347 205 L90 205 Z" fill="url(#allBin)" role="img" aria-label="Photo of a hand placing papers into a shredding bin"/>
      <g stroke="var(--white)" stroke-width="3" fill="none">
        <path d="M96 0 L186 150 L90 205"/>
        <path d="M186 150 L264 106"/>
        <path d="M385 0 L264 106 L347 205"/>
      </g>
      <rect x="555" y="0" width="7" height="205" fill="var(--brand-blue-deep)"/>
    </svg>
    <div class="banner__copy">
      <h2 class="banner__title">Shred, Scan &amp;<br>Store Documents</h2>
      <div class="banner__rule"></div>
      <p class="banner__text">Quick, no contact and affordable<br>paper shredding services in Toronto<br>&amp; Southern Ontario.</p>
      <span class="banner__cta">Get a Quote</span>
    </div>
  </section>

</body>
</html>
```